Postcard Design- Market Update - April 2016

Real Estate Agent. I want to be able to enter data into a postcard (see attached) doesn't have to be exact, but similar and with similar info. I did one postcard with this company already - it may help to see the back of it for how i laid it out.

Target Market(s)

Luxury homes - 800,000- 3,000,000

Industry/Entity Type

Real Estate Agent

Requirements
Must have
• Need to be able to edit the 5 data fields. This is for a luxury market...so it can be a little fanicer.

```html
<!DOCTYPE html>
<html lang="en">
<head>
<meta charset="utf-8">
<title>Area Market Update</title>
<link rel="stylesheet" href="https://fonts.googleapis.com/css2?family=League+Spartan:wght@800&family=Roboto:wght@500;700&display=swap">
<style>
  :root {
    --ink: #1c1210;
    --icon-bg: #7b5049;
    --field-bg: #b3877d;
    --field-edge: #dcc3bc;
    --white: #ffffff;
    --wood-dark: #2a120b;
    --wood-mid: #5a2a1a;
    --wood-light: #7d3f27;
    --glow: #fff8ef;
  }
  * { box-sizing: border-box; margin: 0; padding: 0; }
  html, body { width: 1200px; height: 805px; overflow: hidden; background: var(--white); }
  .postcard {
    position: relative;
    width: 1200px;
    height: 805px;
    overflow: hidden;
    background: radial-gradient(ellipse at 50% 45%, var(--white) 0%, var(--white) 55%, var(--glow) 100%);
    font-family: "Roboto", Arial, sans-serif;
  }
  .door { position: absolute; top: 0; height: 805px; }
  .door--left {
    left: 0; width: 183px;
    background: linear-gradient(90deg, var(--wood-dark) 0%, var(--wood-mid) 45%, var(--wood-light) 80%, #a5643f 100%);
  }
  .door--right {
    right: 0; width: 174px;
    background: linear-gradient(270deg, var(--wood-dark) 0%, var(--wood-mid) 45%, var(--wood-light) 80%, #c58a5e 100%);
  }
  .brand {
    position: absolute;
    top: 78px; left: 0; width: 1200px;
    display: flex; align-items: center; justify-content: center; gap: 16px;
  }
  .brand__dot { width: 64px; height: 64px; border-radius: 50%; background: var(--ink); }
  .brand__name {
    font-family: "League Spartan", "Arial Black", sans-serif;
    font-weight: 800; font-size: 34px; color: var(--ink); letter-spacing: 0.5px;
  }
  .headline {
    font-family: "League Spartan", "Arial Black", sans-serif;
    font-weight: 800; color: var(--ink); text-transform: uppercase;
  }
  .headline__top, .headline__main {
    position: absolute; left: 0; width: 1200px;
    text-align: center; line-height: 1; white-space: nowrap;
  }
  .headline__top { top: 198px; font-size: 92px; letter-spacing: 2px; }
  .headline__main { top: 271px; font-size: 88px; letter-spacing: 0; }
  .stat {
    position: absolute; display: flex; height: 76px;
    border: 2px solid var(--field-edge);
  }
  .stat__icon {
    width: 86px; background: var(--icon-bg);
    display: flex; align-items: center; justify-content: center;
    border-right: 3px solid var(--field-edge);
  }
  .stat__icon svg { width: 42px; height: 42px; }
  .stat__body { flex: 1; background: var(--field-bg); color: var(--white); padding: 6px 14px 0; }
  .stat__value { display: block; font-weight: 700; font-size: 36px; line-height: 38px; letter-spacing: 1px; }
  .stat__label { display: block; font-weight: 500; font-size: 20px; line-height: 24px; white-space: nowrap; }
  .stat--closed { left: 223px; top: 416px; width: 372px; }
  .stat--days { left: 612px; top: 416px; width: 372px; }
  .stat--price { left: 223px; top: 515px; width: 372px; }
  .stat--listings { left: 612px; top: 515px; width: 372px; }
  .stat--change { left: 440px; top: 615px; width: 337px; }
</style>
</head>
<body>
<main class="postcard">
  <div class="door door--left" role="img" aria-label="Photo of an open dark wooden door with a brass handle"></div>
  <div class="door door--right" role="img" aria-label="Photo of an open dark wooden door with a brass handle"></div>

  <header class="brand">
    <span class="brand__dot"></span>
    <span class="brand__name">Veltrane Orwick Homes</span>
  </header>

  <h1 class="headline">
    <span class="headline__top">Area</span>
    <span class="headline__main">Market Update</span>
  </h1>

  <section class="stat stat--closed">
    <div class="stat__icon">
      <svg viewBox="0 0 40 40" fill="#fff"><rect x="4" y="18" width="7" height="16" rx="1"/><path d="M13 18 L20 6 Q23 4 24 8 L22 16 H33 Q36 17 35 21 L32 32 Q31 35 28 35 H13 Z"/><circle cx="7.5" cy="30" r="1.3" fill="#7b5049"/></svg>
    </div>
    <div class="stat__body"><span class="stat__value">XX</span><span class="stat__label">Closed Deals</span></div>
  </section>

  <section class="stat stat--days">
    <div class="stat__icon">
      <svg viewBox="0 0 40 40" fill="none" stroke="#fff" stroke-width="2.5"><rect x="4" y="7" width="32" height="29" rx="2"/><line x1="4" y1="14" x2="36" y2="14"/><line x1="12" y1="3" x2="12" y2="10"/><line x1="28" y1="3" x2="28" y2="10"/><g fill="#fff" stroke="none"><rect x="9" y="18" width="4" height="4"/><rect x="16" y="18" width="4" height="4"/><rect x="23" y="18" width="4" height="4"/><rect x="30" y="18" width="3" height="4"/><rect x="9" y="25" width="4" height="4"/><rect x="16" y="25" width="4" height="4"/><rect x="23" y="25" width="4" height="4"/><rect x="30" y="25" width="3" height="4"/></g></svg>
    </div>
    <div class="stat__body"><span class="stat__value">XX</span><span class="stat__label">Average days on Market</span></div>
  </section>

  <section class="stat stat--price">
    <div class="stat__icon">
      <svg viewBox="0 0 40 40"><text x="20" y="32" text-anchor="middle" font-family="Roboto, Arial, sans-serif" font-weight="700" font-size="32" fill="#fff">$</text></svg>
    </div>
    <div class="stat__body"><span class="stat__value">XX</span><span class="stat__label">Average Sale Price</span></div>
  </section>

  <section class="stat stat--listings">
    <div class="stat__icon">
      <svg viewBox="0 0 40 40" fill="#fff"><path d="M20 5 L37 20 H32 V35 H24 V25 H16 V35 H8 V20 H3 Z"/></svg>
    </div>
    <div class="stat__body"><span class="stat__value">XX</span><span class="stat__label">Homes for Sale</span></div>
  </section>

  <section class="stat stat--change">
    <div class="stat__icon">
      <svg viewBox="0 0 40 40" fill="#fff"><path d="M20 6 L32 20 H24 V34 H16 V20 H8 Z"/></svg>
    </div>
    <div class="stat__body"><span class="stat__value">XX%</span><span class="stat__label">Average Home Price</span></div>
  </section>
</main>
</body>
</html>
```